Plover Freightworks Business Card Design

We are a trucking and warehousing company. We run freight in the US manly from the Pacific NW to TX and back up the the PNW. We also do warehousing where we store, move, and distribute freight. Looking for a clean and modern design of business card. We would like to look rich and elegant. Attached is our logo.

Industry/Entity Type

Trucking Company

Contact Information for Business Card

Looking for a clean and modern design of business card. We would like to look rich and elegant.

Font styles to use
Sans Serif

Colors

Designer to choose colors to be used in the design.

Requirements
Must have
• logo but it should not dominate the card
Should not have
• logo should not dominate the card

```html
<!DOCTYPE html>
<html lang="en">
<head>
<meta charset="utf-8">
<title>Plover Freightworks Business Card</title>
<link rel="stylesheet" href="https://fonts.googleapis.com/css2?family=Roboto+Slab:wght@400;700&display=swap">
<style>
  :root {
    --backdrop: #3a3a3c;
    --card-black: #141414;
    --card-black-soft: #1e1e1e;
    --panel-light: #eeeeee;
    --panel-shade: #d6d6d6;
    --brand-blue: #0f6fa8;
    --ink: #1b1b1b;
    --white: #ffffff;
  }
  * { box-sizing: border-box; margin: 0; padding: 0; }
  html, body {
    width: 1200px; height: 900px; overflow: hidden;
    background: var(--backdrop);
    font-family: "Roboto Slab", Georgia, serif;
  }
  .stage {
    width: 1200px; height: 900px;
    display: flex; align-items: center; justify-content: center; gap: 80px;
  }
  .card {
    position: relative;
    width: 380px; height: 665px;
    background: linear-gradient(160deg, var(--card-black-soft), var(--card-black) 70%);
    box-shadow: 0 18px 40px rgba(0,0,0,.45);
    overflow: hidden;
  }
  /* front */
  .brand {
    position: absolute; top: 120px; left: 0; right: 0;
    display: flex; align-items: center; justify-content: center; gap: 14px;
  }
  .brand-dot { width: 30px; height: 30px; border-radius: 50%; background: var(--brand-blue); flex: none; }
  .brand-name {
    color: var(--white); font-weight: 700; font-size: 24px; line-height: 1.15;
    letter-spacing: .04em; text-transform: uppercase;
  }
  .contact-panel {
    position: absolute; left: 28px; right: 28px; bottom: 28px; height: 330px;
    background: linear-gradient(180deg, var(--panel-light), var(--panel-shade));
    padding: 30px 30px 0 34px;
    color: var(--ink);
  }
  .person-name { color: var(--brand-blue); font-weight: 700; font-size: 21px; letter-spacing: .02em; }
  .person-role { font-size: 13px; margin-top: 2px; }
  .address { font-size: 14px; line-height: 1.45; margin: 18px 0 12px; }
  .contact-list { list-style: none; font-size: 14px; }
  .contact-list li { display: flex; align-items: center; gap: 12px; height: 26px; }
  .contact-list svg { width: 14px; height: 14px; fill: var(--brand-blue); flex: none; }
  .accent { color: var(--brand-blue); }
  /* back */
  .web-ribbon {
    position: absolute; top: 44px; left: 0;
    width: 270px; height: 34px;
    background: var(--brand-blue);
    clip-path: polygon(0 0, 100% 0, 93% 100%, 0 100%);
    color: var(--white); font-size: 13px; font-weight: 700;
    display: flex; align-items: center; padding-left: 26px; letter-spacing: .03em;
  }
  .back-mark {
    position: absolute; inset: 0;
    display: flex; align-items: center; justify-content: center;
    color: var(--brand-blue); font-weight: 700; font-size: 30px;
    text-transform: uppercase; letter-spacing: .05em; text-align: center; line-height: 1.2;
  }
</style>
</head>
<body>
<main class="stage">
  <section class="card card-front">
    <div class="brand">
      <span class="brand-dot"></span>
      <span class="brand-name">Plover<br>Freightworks, LLC</span>
    </div>
    <div class="contact-panel">
      <h1 class="person-name">DANIEL R. WHITCOMBE</h1>
      <p class="person-role">Founder / CEO</p>
      <p class="address">48 Harbour View Lane,<br>Kelburn, Wellington 6012, NZ</p>
      <ul class="contact-list">
        <li><svg viewBox="0 0 24 24"><path d="M6.6 10.8a15 15 0 0 0 6.6 6.6l2.2-2.2a1 1 0 0 1 1-.25 11.4 11.4 0 0 0 3.6.57 1 1 0 0 1 1 1V20a1 1 0 0 1-1 1A17 17 0 0 1 3 4a1 1 0 0 1 1-1h3.5a1 1 0 0 1 1 1c0 1.25.2 2.45.57 3.57a1 1 0 0 1-.25 1z"/></svg>+64 (0)9555 0147</li>
        <li><svg viewBox="0 0 24 24"><path d="M7 1h10a2 2 0 0 1 2 2v18a2 2 0 0 1-2 2H7a2 2 0 0 1-2-2V3a2 2 0 0 1 2-2zm0 3v14h10V4zm5 15.5a1.3 1.3 0 1 0 0 2.6 1.3 1.3 0 0 0 0-2.6z"/></svg>021 555 014</li>
        <li><svg viewBox="0 0 24 24"><path d="M2 5h20v14H2zm2 2v.5l8 5 8-5V7zm0 2.8V17h16V9.8l-8 5z"/></svg>info@<span class="accent">ploverfreightworks</span>.com</li>
        <li><svg viewBox="0 0 24 24"><path d="M12 2a10 10 0 1 0 0 20 10 10 0 0 0 0-20zm6.9 6h-3a15 15 0 0 0-1.3-3.8A8 8 0 0 1 18.9 8zM12 4c.8 1.1 1.5 2.5 1.9 4h-3.8c.4-1.5 1.1-2.9 1.9-4zM4.3 14a8 8 0 0 1 0-4h3.4a16 16 0 0 0 0 4zm.8 2h3a15 15 0 0 0 1.3 3.8A8 8 0 0 1 5.1 16zm3-8h-3a8 8 0 0 1 4.3-3.8C8.8 5.4 8.4 6.7 8.1 8zM12 20c-.8-1.1-1.5-2.5-1.9-4h3.8c-.4 1.5-1.1 2.9-1.9 4zm2.3-6H9.7a14 14 0 0 1 0-4h4.6a14 14 0 0 1 0 4zm.3 5.8c.6-1.2 1-2.4 1.3-3.8h3a8 8 0 0 1-4.3 3.8zm1.7-5.8a16 16 0 0 0 0-4h3.4a8 8 0 0 1 0 4z"/></svg>www.<span class="accent">ploverfreightworks</span>.com</li>
      </ul>
    </div>
  </section>

  <section class="card card-back">
    <div class="web-ribbon">www.ploverfreightworks.com</div>
    <div class="back-mark">Plover<br>Freightworks</div>
  </section>
</main>
</body>
</html>
```